Kelvo Tech Oz Business card revamp

We are looking to revamp our business card design. We are hoping to change our colours to dark navey blue, gray, white and black but are open to keeping the same if a good design is submited. We are after somthing a bit differnt not just boring business card. I have attached a copy of our current card. We Want to keep the same logo design which i have attached a few to hopfully help you in this process. We are after a design that can be personalized to separate 4 people

Colors
0455a3
ffffff
000000
cbcbcb

Requirements
Must have
• Kelvo Tech Logo, address 3/41 Mallory Court, Wexhill 4218, phone number, Name and position

```html
<!DOCTYPE html>
<html lang="en">
<head>
<meta charset="utf-8">
<title>Kelvo Tech Oz – Business Card</title>
<link rel="stylesheet" href="https://fonts.googleapis.com/css2?family=Open+Sans:wght@400;600;700&display=swap">
<style>
  :root {
    --backdrop: #8a8a8a;
    --card-orange: #ef7026;
    --card-white: #ffffff;
    --brand-blue: #2f7fc6;
    --text-light: #ffffff;
    --text-soft: #fbe3d4;
  }
  * { box-sizing: border-box; margin: 0; padding: 0; }
  html, body {
    width: 1200px;
    height: 828px;
    overflow: hidden;
    background: var(--backdrop);
    font-family: "Open Sans", Arial, sans-serif;
  }
  .stage {
    position: relative;
    width: 1200px;
    height: 828px;
  }
  .card {
    position: absolute;
    top: 268px;
    width: 510px;
    height: 292px;
    overflow: hidden;
  }
  .card-back { left: 60px; background: var(--card-orange); }
  .card-front { left: 630px; }

  /* brand wordmark */
  .brand {
    position: absolute;
    display: flex;
    align-items: center;
    gap: 10px;
    color: var(--brand-blue);
    font-weight: 700;
    white-space: nowrap;
  }
  .brand-dot {
    border-radius: 50%;
    background: var(--brand-blue);
    flex: none;
  }
  .card-back .brand {
    left: 0; right: 0;
    top: 92px;
    justify-content: center;
    font-size: 44px;
    letter-spacing: -0.5px;
  }
  .card-back .brand-dot { width: 30px; height: 30px; }

  .back-blurb {
    position: absolute;
    left: 30px; right: 30px;
    top: 208px;
    color: var(--text-light);
    font-size: 12.5px;
    line-height: 17px;
    text-align: center;
  }
  .back-blurb .bullet {
    display: inline-block;
    width: 7px; height: 7px;
    margin: 0 6px 1px;
    border-radius: 50%;
    background: var(--brand-blue);
  }

  /* front face */
  .front-shape { position: absolute; inset: 0; width: 100%; height: 100%; }
  .card-front .brand {
    left: 238px;
    top: 128px;
    font-size: 34px;
    letter-spacing: -0.5px;
  }
  .card-front .brand-dot { width: 22px; height: 22px; }

  .holder {
    position: absolute;
    left: 28px; top: 28px;
    color: var(--text-light);
  }
  .holder-name {
    display: flex;
    align-items: center;
    gap: 8px;
    font-size: 18px;
    font-weight: 600;
  }
  .holder-role {
    margin-left: 22px;
    font-size: 13px;
    color: var(--text-soft);
  }
  .contact-list {
    position: absolute;
    left: 28px; top: 162px;
    list-style: none;
    color: var(--text-light);
    font-size: 12.5px;
    line-height: 17px;
  }
  .contact-list li {
    display: flex;
    align-items: flex-start;
    gap: 9px;
    margin-bottom: 5px;
  }
  .contact-list li.address { margin-bottom: 12px; }
  .icon { width: 13px; height: 13px; flex: none; margin-top: 2px; fill: var(--text-light); }
</style>
</head>
<body>
<main class="stage">

  <section class="card card-back" aria-label="Business card, back">
    <div class="brand"><span class="brand-dot"></span>Kelvo Tech</div>
    <p class="back-blurb">
      Lorem ipsum dolor sit amet <span class="bullet"></span> consectetur adipiscing elit. Proin gravida
      nibh vel velit auctor aliquet <span class="bullet"></span> Aenean sollicitudin, lorem quis
      <span class="bullet"></span> bibendum auctor, nisi elit consequat ipsum.
    </p>
  </section>

  <section class="card card-front" aria-label="Business card, front">
    <svg class="front-shape" viewBox="0 0 510 292" aria-hidden="true">
      <rect width="510" height="292" fill="var(--card-orange)"/>
      <path d="M267 0 H510 V292 H288 A168 168 0 0 1 267 0 Z" fill="var(--card-white)"/>
      <path d="M257 1 A173 173 0 0 0 405 307" fill="none" stroke="var(--brand-blue)" stroke-width="9"/>
    </svg>

    <div class="holder">
      <div class="holder-name">
        <svg class="icon" viewBox="0 0 16 16"><circle cx="8" cy="5" r="3.5"/><path d="M1.5 15c0-4 3-6 6.5-6s6.5 2 6.5 6z"/></svg>
        Daniel Harlow
      </div>
      <div class="holder-role">Owner</div>
    </div>

    <ul class="contact-list">
      <li class="address">
        <svg class="icon" viewBox="0 0 16 16"><path d="M8 0a5.5 5.5 0 0 0-5.5 5.5C2.5 10 8 16 8 16s5.5-6 5.5-10.5A5.5 5.5 0 0 0 8 0zm0 8a2.5 2.5 0 1 1 0-5 2.5 2.5 0 0 1 0 5z"/></svg>
        <span>3/41 Mallory Court<br>Wexhill 4218</span>
      </li>
      <li>
        <svg class="icon" viewBox="0 0 16 16"><path d="M3.6 0.8l2.3 2.9c.4.5.3 1.2-.1 1.6L4.6 6.5c.9 2 2.5 3.7 4.5 4.7l1.3-1.2c.4-.4 1.1-.4 1.6 0l2.9 2.3c.5.4.5 1.2 0 1.7l-1.4 1.4C11.4 17.5.1 6.2 1.7 2.1L3 .8c.2-.2.4-.2.6 0z"/></svg>
        <span>361 480 2295</span>
      </li>
      <li>
        <svg class="icon" viewBox="0 0 16 16"><path d="M1 3h14v10H1z M1.8 3.8 8 8.6l6.2-4.8" fill="none" stroke="var(--text-light)" stroke-width="1.6"/></svg>
        <span>daniel@kelvotech.com.au</span>
      </li>
      <li>
        <svg class="icon" viewBox="0 0 16 16"><circle cx="8" cy="8" r="7" fill="none" stroke="var(--text-light)" stroke-width="1.6"/><path d="M1 8h14M8 1c-3 3.5-3 10.5 0 14M8 1c3 3.5 3 10.5 0 14" fill="none" stroke="var(--text-light)" stroke-width="1.3"/></svg>
        <span>www.kelvotech.com.au</span>
      </li>
    </ul>

    <div class="brand"><span class="brand-dot"></span>Kelvo Tech</div>
  </section>

</main>
</body>
</html>
```